Christmas Party Poster

I am promoting a Christmas Party for teenagers age 13-17 years old. The event is the first of its kind in our area, Weston Super Mare. The ticket price is to include food, soft drink's, music, entertainment.

There is nothing else of its kind in the the area or surrounding towns so a one of a kind event and new to the town. I would like the poster to be as simple and less busy as possible while still clearly showing the key information, anything that can be added it to show its a Christmas party for teenagers would be great. Also this is aimed at 13-17 year old's so as current and modern a design as possible.
Updates

A big thank you for the designs so far, As this is my first project I'm just getting the hang of what to ask for. I have slightly updated the brief and I now realize less is more, so long as the poster has the key elements of event name, date, time's, location, price and age range. The rest I should have been more flexible on. Thank you for your patience.

Target Market(s)

My Target Market are teenagers specifically 13-17 year olds

Industry/Entity Type

Town

Requirements
Must have
• The Title 'Frostlark' The venue is 'The Amber Pavilion w-s-m', Phone Number '01934 582093' Date '19th December'. Times '19.00 - 23.00'. Strictly u18 or age 13-17 years. Ticket price of £20. Face book 'frost lark wsm' limited 4 tickets per person
Nice to have
• Christmas Party, Photo of your night out. Food and drink included
Should not have
• no worded reference to Santa, snowmen, reindeer, disco, try to keep out as not to offend cool teenagers.

```html
<!DOCTYPE html>
<html lang="en">
<head>
<meta charset="utf-8">
<title>Frostlark – The Amber Pavilion WSM</title>
<link rel="stylesheet" href="https://fonts.googleapis.com/css2?family=Comfortaa:wght@400;700&family=Arimo:wght@700&family=Oswald:wght@500&display=swap">
<style>
  :root {
    --ice-white: #ffffff;
    --frost-cyan: #7fe3f5;
    --sky-blue: #2fa6f0;
    --deep-blue: #1d4fe8;
    --violet-blue: #3a2fd8;
    --title-blue: #3f55c8;
    --title-violet: #5a4fb0;
    --navy: #26307e;
    --ink: #0a0a14;
    --glow: rgba(255,255,255,0.9);
  }
  html, body { margin: 0; padding: 0; overflow: hidden; background: var(--ice-white); }
  .poster {
    position: relative;
    width: 900px; height: 1200px;
    overflow: hidden;
    background: var(--ice-white);
    font-family: "Arimo", Arial, sans-serif;
    font-weight: 700;
  }
  .poster * { position: absolute; margin: 0; white-space: nowrap; font-weight: 700; }

  .burst-backdrop {
    left: 0; top: 0; width: 900px; height: 520px;
    background:
      radial-gradient(circle at 140px 60px, rgba(127,227,245,0.25), transparent 130px),
      radial-gradient(circle at 500px 60px, rgba(127,227,245,0.18), transparent 110px),
      radial-gradient(circle at 780px 110px, rgba(127,227,245,0.22), transparent 130px),
      radial-gradient(circle at 720px 320px, rgba(127,227,245,0.18), transparent 110px);
  }
  .crowd-lights {
    left: 0; top: 420px; width: 900px; height: 780px;
    background:
      radial-gradient(ellipse 420px 260px at 180px 1000px, rgba(60,40,220,0.55), transparent),
      linear-gradient(180deg, rgba(255,255,255,0) 0%, #bdf2fb 12%, var(--frost-cyan) 28%, var(--sky-blue) 55%, var(--deep-blue) 80%, var(--violet-blue) 100%);
  }

  .title-the {
    left: 172px; top: 178px;
    font-family: "Comfortaa", sans-serif;
    font-size: 34px; line-height: 1; color: var(--title-violet); letter-spacing: 1px;
  }
  .title-name {
    left: 50px; top: 212px; width: 800px; text-align: center;
    font-family: "Comfortaa", sans-serif;
    font-size: 150px; letter-spacing: -5px; line-height: 1;
    color: var(--title-blue);
    text-shadow: 0 2px 0 #c9d2ff, 0 -2px 0 #1c2a86, 4px 6px 8px rgba(20,30,90,0.35);
  }
  .venue {
    left: 75px; top: 386px;
    font-family: "Comfortaa", sans-serif;
    font-size: 30px; line-height: 36px; color: var(--ink); text-transform: uppercase; letter-spacing: 1px;
  }
  .venue span { position: static; display: block; padding-left: 4px; }
  .event-date {
    left: 79px; top: 466px;
    font-family: "Comfortaa", sans-serif;
    font-size: 24px; color: var(--navy);
  }

  .side-photos {
    left: 422px; top: 484px; height: 230px;
    writing-mode: vertical-rl; transform: rotate(180deg);
    font-family: "Comfortaa", sans-serif;
    font-size: 32px; color: #3a5fb0;
  }
  .side-party {
    left: 478px; top: 500px; height: 392px;
    writing-mode: vertical-rl; transform: rotate(180deg);
    font-family: "Comfortaa", sans-serif;
    font-size: 22px; color: var(--navy);
  }

  .fountain {
    right: 128px; top: 560px; text-align: right;
    font-family: "Comfortaa", sans-serif;
    font-size: 25px; line-height: 38px; color: var(--navy);
    text-shadow: 0 0 6px var(--glow), 0 0 10px var(--glow);
  }
  .fountain span { position: static; display: block; }
  .fountain-amp {
    left: 778px; top: 552px;
    font-family: "Comfortaa", sans-serif;
    font-size: 72px; line-height: 1; color: var(--deep-blue);
    text-shadow: 0 0 8px var(--glow), 0 0 14px var(--glow);
  }

  .times { right: 86px; top: 650px; font-size: 17px; color: var(--ice-white); }
  .ages { right: 92px; top: 694px; font-size: 36px; line-height: 1; color: var(--ink); }
  .ages-sub { right: 92px; top: 729px; font-size: 24px; color: var(--ink); }
  .price-lead { left: 560px; top: 774px; font-size: 21px; line-height: 24px; color: var(--ice-white); text-align: right; text-shadow: 0 0 6px rgba(30,60,200,0.8); }
  .price { left: 652px; top: 762px; font-size: 72px; line-height: 1; color: var(--ice-white); text-shadow: 0 0 10px rgba(40,60,200,0.8); }
  .price-note { right: 92px; top: 838px; font-size: 48px; line-height: 1; color: var(--ink); }

  .top-tunes {
    left: 100px; top: 710px;
    font-family: "Comfortaa", sans-serif;
    font-size: 56px; color: var(--ice-white);
  }
  .face-art {
    right: 460px; top: 808px; text-align: right;
    font-family: "Comfortaa", sans-serif;
    font-size: 26px; line-height: 30px; color: var(--ice-white);
  }
  .face-art span { position: static; display: block; font-size: 16px; line-height: 24px; }

  .inclusions { right: 92px; top: 896px; text-align: right; font-size: 25px; line-height: 44px; color: var(--ice-white); }
  .inclusions span { position: static; display: block; }
  .welcome { right: 92px; top: 998px; text-align: right; font-size: 21px; color: var(--ice-white); }
  .welcome-note { right: 92px; top: 1031px; font-size: 13px; color: var(--ink); }

  .ticket-limit {
    left: 820px; top: 780px; height: 280px;
    writing-mode: vertical-rl;
    font-family: "Comfortaa", sans-serif;
    font-size: 21px; color: var(--ice-white);
  }

  .box-office {
    left: 650px; top: 1076px;
    font-family: "Oswald", "Arial Narrow", sans-serif;
    font-size: 26px; line-height: 36px; color: var(--ice-white);
  }
  .box-office span { position: static; display: block; font-weight: 500; }

  .social { left: 38px; top: 1110px; display: flex; align-items: center; }
  .social-mark { position: static; width: 46px; height: 46px; border-radius: 6px; background: var(--deep-blue); box-shadow: 0 0 0 2px rgba(255,255,255,0.4); }
  .social-handle { position: static; margin-left: 16px; font-size: 19px; color: var(--ice-white); }
</style>
</head>
<body>
<main class="poster">
  <div class="burst-backdrop" role="img" aria-label="Faint pale blue snowflake bursts on white"></div>
  <div class="crowd-lights" role="img" aria-label="Party crowd silhouettes with bokeh light dots in cyan and blue"></div>

  <p class="title-the">THE</p>
  <h1 class="title-name">Frostlark</h1>

  <p class="venue"><span>The Amber Pavilion</span><span>WSM</span></p>
  <p class="event-date">19th December</p>

  <p class="side-photos">cool photos</p>
  <p class="side-party">the party to be seen at</p>

  <p class="fountain"><span>chocolate</span><span>cocktail fountain</span></p>
  <p class="fountain-amp">&amp;</p>

  <p class="times">19.00pm - 23.00pm</p>
  <p class="ages">13-17 only</p>
  <p class="ages-sub">under18s</p>
  <p class="price-lead">all this<br>for only</p>
  <p class="price">£20</p>
  <p class="price-note">all in</p>

  <p class="top-tunes">top tunes</p>
  <p class="face-art">wicked face art<span>and loads more</span></p>

  <p class="inclusions"><span>entrance, all you can eat &amp; drink</span><span>and as much dance &amp; fun you can handle</span></p>
  <p class="welcome">champagne cocktail when you get here</p>
  <p class="welcome-note">alcohol free of course</p>

  <p class="ticket-limit">limited to 4 tickets pp</p>

  <p class="box-office"><span>Contact Box Office</span><span>01934 582093 soon!!</span></p>

  <div class="social">
    <span class="social-mark"></span>
    <span class="social-handle">frost lark wsm</span>
  </div>
</main>
</body>
</html>
```